Plakate für eine Veranstaltung
Sehr professionelle Umsetzung, schnelle Absprachen und freundlicher Kontakt. Immer wieder gerne, vielen Dank lieber Pravello.
Zielgruppe
Musikerin / Sängerin, Wir suchen ein hochwertiges Plakat mit unseren Specials Guests für ein Publikum mittleren Alters.
Aufgabenstellung
Anlage in Din1, Titel der Veranstaltung: 'Lanterns over Snowfields' - Marlene Kottwitz & Friends in concert, hochauflösende Bilder sind fast komplett vorhanden, gerne erst mal mit vorhandenen Material Idee kreieren und im Anschluss austauschen. Details zum Konzert: 16.11.23, Theater am Brunnenhügel Lingen, 19.30 Uhr, Veranstalter: Stadt Lingen. Gerne die Hauptsängerin im Fokus und die anderen Aktiven in Einblendung einarbeiten. Name der Special Guest stehen als Dateiname in den angehängten Files.

```html
<!DOCTYPE html>
<html lang="de">
<head>
<meta charset="utf-8">
<title>Marlene Kottwitz &amp; Friends – Lanterns over Snowfields</title>
<link href="https://fonts.googleapis.com/css2?family=Archivo:wght@700;800&family=Abril+Fatface&family=Dancing+Script:wght@600;700&family=Figtree:wght@400;600;700&display=swap" rel="stylesheet">
<style>
  :root {
    --page: #ffffff;
    --plum: #3a1b34;
    --plum-deep: #2a1227;
    --band: #22061a;
    --dusk-blue: #3d4a66;
    --cream: #e0d2a6;
    --copper: #d9b08c;
    --white: #ffffff;
  }
  * { margin: 0; padding: 0; box-sizing: border-box; }
  html, body { width: 1000px; height: 1200px; overflow: hidden; background: var(--page); }
  .poster {
    position: absolute; left: 89px; top: 20px; width: 821px; height: 1160px;
    background: radial-gradient(ellipse at 45% 62%, #55304c 0%, var(--plum) 45%, var(--plum-deep) 100%);
    overflow: hidden;
    color: var(--white);
  }
  .hero {
    position: absolute; left: 0; top: 0; width: 821px; height: 452px;
    background: linear-gradient(100deg, #2b1226 0%, #4a2443 45%, var(--dusk-blue) 100%);
    overflow: hidden;
  }
  .hero-photo {
    position: absolute; left: -50px; top: 44px; width: 490px; height: 490px; border-radius: 50%;
    background: radial-gradient(circle at 40% 45%, #b07a4a 0%, #5a2a2c 40%, #1e0a14 80%);
  }
  .reel {
    position: absolute; left: 694px; top: 8px; width: 126px; height: 142px;
    background: linear-gradient(135deg, rgba(217,176,140,.55), rgba(217,176,140,.2));
    border-radius: 40% 20% 45% 30%;
  }
  .headliner {
    position: absolute; right: 23px; top: 176px;
    font-family: "Archivo", sans-serif; font-weight: 800; font-size: 60px; line-height: 1;
    letter-spacing: -0.5px; white-space: nowrap;
  }
  .friends, .in-concert {
    position: absolute; font-family: "Dancing Script", cursive; font-weight: 700; white-space: nowrap; line-height: 1;
  }
  .friends { right: 98px; top: 255px; font-size: 78px; }
  .in-concert { right: 58px; top: 338px; font-size: 66px; }
  .title-band {
    position: absolute; left: 0; top: 452px; width: 821px; height: 194px; background: var(--band);
  }
  .title-line {
    position: absolute; font-family: "Abril Fatface", serif; color: var(--cream);
    font-size: 66px; line-height: 1; letter-spacing: 1px; white-space: nowrap;
  }
  .title-line.first { left: 113px; top: 478px; }
  .title-line.second { right: 90px; top: 560px; }
  .title-small {
    font-family: "Dancing Script", cursive; font-weight: 700; color: var(--white);
    font-size: 62px; letter-spacing: 0; margin-left: 14px;
  }
  .guest { position: absolute; top: 657px; width: 260px; text-align: center; }
  .guest-photo { width: 196px; height: 196px; border-radius: 50%; margin: 0 auto; }
  .guest-photo.violin { background: radial-gradient(circle at 45% 55%, #b3335a 0%, #4a1020 55%, #1a0a0e 100%); }
  .guest-photo.piano { background: radial-gradient(circle at 50% 55%, #6b5a52 0%, #2a2224 45%, #f4f4f4 46%, #ffffff 100%); }
  .guest-photo.pipes { background: radial-gradient(circle at 40% 55%, #2f4a7a 0%, #1b2a3c 50%, #3f6a3a 100%); }
  .guest-role {
    font-family: "Dancing Script", cursive; font-weight: 700; color: var(--copper);
    font-size: 40px; line-height: 1; margin-top: 10px; white-space: nowrap;
  }
  .guest-name {
    font-family: "Archivo", sans-serif; font-weight: 700; font-size: 19px; line-height: 1;
    margin-top: 6px; letter-spacing: -0.2px; white-space: nowrap;
  }
  .rule { position: absolute; left: 31px; width: 758px; height: 3px; background: var(--white); }
  .rule.top { top: 950px; }
  .rule.bottom { top: 1130px; }
  .divider { position: absolute; left: 244px; top: 963px; width: 3px; height: 155px; background: var(--white); }
  .date-big {
    position: absolute; left: 42px; top: 970px;
    font-family: "Figtree", sans-serif; font-weight: 700; font-size: 76px; line-height: 1; letter-spacing: -2px;
  }
  .time-script {
    position: absolute; left: 46px; top: 1052px;
    font-family: "Dancing Script", cursive; font-weight: 600; color: var(--copper); font-size: 44px; line-height: 1;
  }
  .details {
    position: absolute; right: 51px; top: 972px; text-align: right;
    font-family: "Figtree", sans-serif; line-height: 1; white-space: nowrap;
  }
  .details .when { font-weight: 700; font-size: 39px; }
  .details .venue { font-weight: 400; font-size: 36px; margin-top: 12px; }
  .details .city { font-weight: 400; font-size: 36px; margin-top: 13px; }
</style>
</head>
<body>
  <main class="poster">
    <section class="hero">
      <div class="hero-photo" role="img" aria-label="Foto der Sängerin mit Mikrofon auf der Bühne"></div>
      <div class="reel" role="img" aria-label="Illustration einer Filmrolle"></div>
    </section>
    <h1 class="headliner">MARLENE KOTTWITZ</h1>
    <p class="friends">&amp; Friends</p>
    <p class="in-concert">in Concert</p>

    <section class="title-band"></section>
    <h2 class="title-line first">LANTERNS<span class="title-small">over</span></h2>
    <p class="title-line second">SNOWFIELDS</p>

    <div class="guest" style="left:15px">
      <div class="guest-photo violin" role="img" aria-label="Foto der Violinistin mit Lasershow"></div>
      <p class="guest-role">Violistin</p>
      <p class="guest-name">ILKA WENDRATH</p>
    </div>
    <div class="guest" style="left:280px">
      <div class="guest-photo piano" role="img" aria-label="Porträtfoto des Pianisten"></div>
      <p class="guest-role">Pianist</p>
      <p class="guest-name">TOBIAS RENWALD</p>
    </div>
    <div class="guest" style="left:544px">
      <div class="guest-photo pipes" role="img" aria-label="Foto eines Dudelsackspielers in Highland-Tracht"></div>
      <p class="guest-role">Pipes &amp; Drums</p>
      <p class="guest-name">Vechte-Highlander</p>
    </div>

    <div class="rule top"></div>
    <p class="date-big">16/11</p>
    <p class="time-script">19.30 Uhr</p>
    <div class="divider"></div>
    <div class="details">
      <p class="when">16.11. 2023, 19.30 Uhr</p>
      <p class="venue">Theater am Brunnenhügel</p>
      <p class="city">in Lingen</p>
    </div>
    <div class="rule bottom"></div>
  </main>
</body>
</html>
```